Bright Tutor Hub business card

Use existing logo to design a business card which contains information that is listed below. Use of logo as attached. It is important that the colour scheme matches the logo already designed. It needs to be crisp and professional. This is an on line business, a database of training providers for educational establishments. The website will provide users with full information on trainers who are available and their credibility.
Target Market(s)
Educators and training providers
Industry/Entity Type
Education
Contact Information for Business Card
Font styles to use
Colors
Designer to choose colors to be used in the design.
Requirements
Must have
- Email address mara@brighttutorhub.co.uk
- Twitter feed. @MaraBth
- LinkedIn details Mara Fenwick
- Mobile phone number 07812 459302
- Mission statement: To create a learning network that ensures that schools receive first class training that is excellent value for money.
Nice to have
- N/a
Should not have
- Twee educational images

```html
<!DOCTYPE html>
<html lang="en">
<head>
<meta charset="utf-8">
<title>Bright Tutor Hub – Business Card</title>
<link rel="stylesheet" href="https://fonts.googleapis.com/css2?family=Roboto:wght@400;500;700&display=swap">
<style>
  :root {
    --stage: #2a2a2a;
    --brand-blue: #29a8e0;
    --brand-deep: #1c77c3;
    --card-white: #ffffff;
    --ink: #333333;
    --ink-soft: #555555;
    --rule: #6b6b6b;
  }
  html, body {
    margin: 0;
    padding: 0;
    width: 1200px;
    height: 873px;
    overflow: hidden;
    background: var(--stage);
    font-family: "Roboto", Arial, sans-serif;
  }
  .stage {
    position: relative;
    width: 1200px;
    height: 873px;
  }
  .card {
    position: absolute;
    width: 520px;
    height: 300px;
    border-radius: 22px;
    box-sizing: border-box;
  }

  /* Front: mission side */
  .card--front {
    left: 70px;
    top: 130px;
    background: var(--brand-blue);
    color: var(--card-white);
    text-align: center;
  }
  .front-brand {
    position: absolute;
    left: 0;
    right: 0;
    top: 70px;
    display: flex;
    align-items: center;
    justify-content: center;
    gap: 14px;
  }
  .brand-dot {
    width: 44px;
    height: 44px;
    border-radius: 50%;
    background: var(--card-white);
    flex: none;
  }
  .front-brand .brand-name {
    font-size: 40px;
    font-weight: 700;
    letter-spacing: 0.5px;
    color: var(--card-white);
    white-space: nowrap;
  }
  .mission {
    position: absolute;
    left: 40px;
    right: 40px;
    top: 160px;
  }
  .mission-title {
    margin: 0 0 6px;
    font-size: 13px;
    font-weight: 500;
    letter-spacing: 0.5px;
    text-transform: uppercase;
  }
  .mission-text {
    margin: 0;
    font-size: 14px;
    line-height: 1.4;
  }

  /* Back: contact side */
  .card--back {
    left: 610px;
    top: 440px;
    background: var(--card-white);
    color: var(--ink);
  }
  .rule {
    position: absolute;
    height: 1px;
    background: var(--rule);
  }
  .rule--top { left: 300px; right: 24px; top: 62px; }
  .rule--bottom { left: 24px; right: 200px; top: 205px; }
  .back-brand {
    position: absolute;
    left: 28px;
    top: 112px;
    display: flex;
    align-items: center;
    gap: 10px;
  }
  .back-brand .brand-dot {
    width: 34px;
    height: 34px;
    background: var(--brand-deep);
  }
  .back-brand .brand-name {
    font-size: 26px;
    font-weight: 700;
    color: var(--brand-deep);
    white-space: nowrap;
  }
  .contact-list {
    position: absolute;
    margin: 0;
    padding: 0;
    list-style: none;
    font-size: 15px;
    color: var(--ink);
  }
  .contact-list li {
    display: flex;
    align-items: center;
    gap: 10px;
    height: 27px;
    white-space: nowrap;
  }
  .contact-list--direct { left: 28px; top: 218px; }
  .contact-list--social { left: 330px; top: 76px; font-size: 14px; color: var(--ink-soft); }
  .icon {
    width: 19px;
    height: 19px;
    border-radius: 3px;
    background: var(--brand-deep);
    display: inline-flex;
    align-items: center;
    justify-content: center;
    flex: none;
  }
  .icon svg { width: 13px; height: 13px; }
</style>
</head>
<body>
<main class="stage">

  <section class="card card--front" aria-label="Business card front">
    <div class="front-brand">
      <span class="brand-dot" aria-hidden="true"></span>
      <span class="brand-name">Bright Tutor Hub</span>
    </div>
    <div class="mission">
      <h2 class="mission-title">Mission Statement</h2>
      <p class="mission-text">To create a learning network that ensures that schools receive first class training that is excellent value for money.</p>
    </div>
  </section>

  <section class="card card--back" aria-label="Business card back">
    <div class="rule rule--top"></div>

    <div class="back-brand">
      <span class="brand-dot" aria-hidden="true"></span>
      <span class="brand-name">Bright Tutor Hub</span>
    </div>

    <ul class="contact-list contact-list--social">
      <li>
        <span class="icon" aria-hidden="true">
          <svg viewBox="0 0 24 24"><circle cx="12" cy="12" r="4" fill="none" stroke="#fff" stroke-width="2.4"/><path d="M16 8v5.5a2.5 2.5 0 0 0 5 0V12a9 9 0 1 0-3.5 7.1" fill="none" stroke="#fff" stroke-width="2.4" stroke-linecap="round"/></svg>
        </span>@MaraBth
      </li>
      <li>
        <span class="icon" aria-hidden="true">
          <svg viewBox="0 0 24 24"><rect x="3" y="7" width="18" height="13" rx="1.5" fill="none" stroke="#fff" stroke-width="2.2"/><path d="M9 7V5h6v2M3 12h18" fill="none" stroke="#fff" stroke-width="2.2"/></svg>
        </span>details Mara Fenwick
      </li>
    </ul>

    <div class="rule rule--bottom"></div>

    <ul class="contact-list contact-list--direct">
      <li>
        <span class="icon" aria-hidden="true">
          <svg viewBox="0 0 24 24"><path fill="#fff" d="M6.6 10.8a15.1 15.1 0 0 0 6.6 6.6l2.2-2.2a1 1 0 0 1 1-.25 11.4 11.4 0 0 0 3.6.57 1 1 0 0 1 1 1V20a1 1 0 0 1-1 1A17 17 0 0 1 3 4a1 1 0 0 1 1-1h3.5a1 1 0 0 1 1 1c0 1.25.2 2.45.57 3.57a1 1 0 0 1-.25 1z"/></svg>
        </span>07812 459302
      </li>
      <li>
        <span class="icon" aria-hidden="true">
          <svg viewBox="0 0 24 24"><rect x="2" y="5" width="20" height="14" rx="1" fill="none" stroke="#fff" stroke-width="2"/><path d="M2 6l10 7 10-7" fill="none" stroke="#fff" stroke-width="2"/></svg>
        </span>mara@brighttutorhub.co.uk
      </li>
    </ul>
  </section>

</main>
</body>
</html>
```